Web design for business website

I need a web design for a business website for one of our clients who is specialized in alarm management software. I would like you to design 3 web pages, one for each of the 3 pages. You need to process the corporate identity of our client to the web design. This means the colors of the logo (red and black) should definitely show up on all of the 3 pages. Find the logo file for the logo of our customer. To increase readability I suggest you use a white/light background. All suggestions are welcome.

Please kindly download atttached Webdesign.zip and read the project brief first. The project brief refers to all other files of the zip file. Your design must have exactly the same structure as the wireframes.
Updates

Target Market(s)

B2B, Alarm management

Industry/Entity Type

Business

Number of Pages Required

3 page

Requirements
Must have
• The web design must have exactly the same structure as the wireframes and needs to contain the colors of the company logo.

```html
<!DOCTYPE html>
<html lang="en">
<head>
<meta charset="utf-8">
<title>Veritrace – Alarm Management Software</title>
<link href="https://fonts.googleapis.com/css2?family=Lato:wght@400;700&family=Oswald:wght@400&family=Arimo:wght@700&family=Kaushan+Script&family=Roboto:wght@400&display=swap" rel="stylesheet">
<style>
:root{
  --red:#e8401c;
  --ink:#1b1f2a;
  --text:#333;
  --footer:#0a1220;
  --footer-line:#1d2636;
  --white:#fff;
}
*{box-sizing:border-box;margin:0;padding:0}
html,body{width:932px;height:1200px;overflow:hidden;background:var(--white)}
body{position:relative;font-family:'Lato',sans-serif;color:var(--text)}
.abs{position:absolute}

/* header */
.brand{left:101px;top:16px}
.brand-name{font-family:'Lato',sans-serif;font-weight:700;font-size:32px;color:var(--ink);line-height:1}
.brand-tag{font-size:11px;color:var(--ink);margin-top:6px;letter-spacing:.2px}
.phone{left:484px;top:11px;display:flex;align-items:center;gap:8px;font-weight:700;font-size:14px;color:var(--ink)}
.lang{left:636px;top:8px;width:64px;height:20px;border:1px solid #ccc;font-size:11px;color:#888;padding:3px 8px}
.lang::after{content:"";position:absolute;right:8px;top:6px;width:4px;height:4px;border-right:1px solid #555;border-bottom:1px solid #555;transform:rotate(45deg)}
.search{left:707px;top:8px;width:123px;height:20px;border:1px solid #bbb;font-size:11px;font-style:italic;color:#666;padding:3px 6px}
.search-btn{position:absolute;right:-1px;top:-1px;width:21px;height:20px;background:#333;display:flex;align-items:center;justify-content:center}
.account{top:46px;font-size:12.5px;color:var(--ink)}
.account.login{color:var(--red);text-decoration:underline}
.nav{left:101px;top:86px;width:729px;display:flex;justify-content:space-between;font-size:12.5px;font-weight:700;letter-spacing:.3px;color:var(--ink)}
.nav .active{color:var(--red);font-weight:400}
.nav-sep{top:88px;width:1px;height:12px;background:#ddd}

/* hero */
.hero{left:0;top:107px;width:932px;height:430px;background:linear-gradient(180deg,#8fa1ac 0%,#c9b58d 35%,#e8a64a 55%,#7c8a55 72%,#3c4a2c 100%)}
.hero-title{left:0;top:436px;width:932px;text-align:center;font-family:'Oswald',sans-serif;font-weight:400;font-size:25px;letter-spacing:-.2px;color:var(--white);text-shadow:0 1px 3px rgba(0,0,0,.5)}
.hero-band{left:0;top:478px;width:932px;height:59px;background:rgba(30,30,30,.72)}
.thumb{top:492px;width:88px;height:77px;border:3px solid var(--white)}
.thumb.current{border-color:var(--red)}
.thumb-pointer{left:193px;top:484px;width:0;height:0;border-left:8px solid transparent;border-right:8px solid transparent;border-bottom:8px solid var(--red)}

/* about */
.about-rule{left:446px;top:612px;width:40px;height:4px;background:var(--red);border-radius:2px}
.section-title{left:0;width:932px;text-align:center;font-family:'Arimo',sans-serif;font-weight:700;color:#111}
.section-title em{font-style:normal;color:var(--red)}
.about-text{left:102px;top:670px;width:728px;text-align:center;font-size:10.8px;line-height:16.5px;color:#444}
.read-more{left:0;top:777px;width:932px;text-align:center;font-size:12px;font-weight:700;color:#333;text-decoration:underline;letter-spacing:.3px}

/* clients */
.clients{left:101px;top:853px;width:729px;height:79px;border:1px solid #ccc;border-radius:5px}
.arrow{top:884px;width:17px;height:17px;background:#333;border-radius:2px;display:flex;align-items:center;justify-content:center}
.client{top:878px;display:flex;align-items:center;gap:6px;font-weight:700;font-size:15px;color:#555;height:30px}
.client i{display:block;width:22px;height:22px;border-radius:50%;background:#c9c9c9}

/* footer */
.footer{left:0;top:954px;width:932px;height:218px;background:var(--footer)}
.footer-rule{left:0;top:1004px;width:932px;height:1px;background:var(--footer-line)}
.follow{left:101px;top:964px;font-family:'Kaushan Script',cursive;font-size:17px;color:var(--white)}
.social{top:964px;width:25px;height:25px;border-radius:50%;background:#2c3648}
.news-icon{left:382px;top:958px;width:38px;height:38px;border-radius:50%;border:2px solid var(--white);display:flex;align-items:center;justify-content:center}
.news-label{left:427px;top:967px;font-family:'Roboto',sans-serif;font-size:15px;color:var(--white)}
.news-rule{left:427px;top:987px;width:46px;height:2px;background:var(--red)}
.email{left:557px;top:966px;width:196px;height:23px;background:var(--white);border-radius:2px;font-size:11px;font-style:italic;color:#444;padding:5px 8px}
.subscribe{left:760px;top:966px;width:70px;height:23px;background:var(--red);border-radius:2px;color:var(--white);font-size:11px;font-weight:700;text-align:center;line-height:23px}
.col{top:1019px;color:var(--white)}
.col h4{font-weight:400;font-size:14px;letter-spacing:.3px;padding-bottom:5px;border-bottom:1px dotted #4a5467;width:122px;margin-bottom:9px}
.col li{list-style:none;font-size:10px;line-height:11px;margin-bottom:12px;color:#e8e8e8}
.col li::before{content:"• "}
.contact li{display:flex;gap:10px;list-style:none;font-size:10px;line-height:12px;margin-bottom:8px}
.contact li::before{content:none}
.contact svg{flex:none;margin-top:1px}
.other{display:block;font-size:11px;font-weight:700;text-decoration:underline;margin-left:25px;margin-top:-2px;color:var(--white)}
.copyright{left:0;top:1172px;width:932px;height:28px;background:var(--red);color:var(--white);font-size:9px;font-weight:700;text-align:center;line-height:28px}
</style>
</head>
<body>

<header>
  <div class="abs brand">
    <div class="brand-name">Veritrace</div>
    <div class="brand-tag">Alarm insight for operations</div>
  </div>
  <div class="abs phone">
    <svg width="14" height="14" viewBox="0 0 24 24"><path fill="#e8401c" d="M6.6 10.8a15 15 0 0 0 6.6 6.6l2.2-2.2c.3-.3.7-.4 1-.2 1.1.4 2.3.6 3.6.6.6 0 1 .4 1 1V20c0 .6-.4 1-1 1A17 17 0 0 1 3 4c0-.6.4-1 1-1h3.5c.6 0 1 .4 1 1 0 1.3.2 2.5.6 3.6.1.3 0 .7-.2 1z"/></svg>
    +31 (0)20 5550 184
  </div>
  <div class="abs lang">English</div>
  <div class="abs search">Search
    <span class="search-btn"><svg width="11" height="11" viewBox="0 0 12 12"><circle cx="5" cy="5" r="3.5" fill="none" stroke="#fff" stroke-width="1.6"/><line x1="7.6" y1="7.6" x2="11" y2="11" stroke="#fff" stroke-width="1.8"/></svg></span>
  </div>
  <span class="abs account" style="left:665px">Account</span>
  <span class="abs account login" style="left:735px">Log in</span>
  <span class="abs account" style="left:792px">Sign up</span>

  <nav class="abs nav">
    <span class="active">HOME</span><span>INDUSTRY</span><span>TELECOM</span><span>POWER</span><span>UTILITIES</span><span>INFRA</span><span>STORE</span>
  </nav>
  <span class="abs nav-sep" style="left:170px"></span>
  <span class="abs nav-sep" style="left:298px"></span>
  <span class="abs nav-sep" style="left:421px"></span>
  <span class="abs nav-sep" style="left:532px"></span>
  <span class="abs nav-sep" style="left:654px"></span>
  <span class="abs nav-sep" style="left:757px"></span>
</header>

<section>
  <div class="abs hero" role="img" aria-label="Photo of an oil refinery at sunset behind a marsh"></div>
  <h1 class="abs hero-title">Our Business Is Specialized Alarm Management Software</h1>
  <div class="abs hero-band"></div>
  <span class="abs thumb-pointer"></span>
  <div class="abs thumb current" style="left:157px;background:linear-gradient(#a9b3b5,#d7a255 55%,#4d5a38)" role="img" aria-label="Refinery at sunset thumbnail"></div>
  <div class="abs thumb" style="left:262px;background:linear-gradient(#3d6ca8,#d2b14a 60%,#5a6a80)" role="img" aria-label="Industrial plant at night thumbnail"></div>
  <div class="abs thumb" style="left:368px;background:linear-gradient(#e2a060,#c87840 55%,#9c6a50)" role="img" aria-label="Highway interchange at dusk thumbnail"></div>
  <div class="abs thumb" style="left:474px;background:linear-gradient(#d5dde4,#8fb4cf 55%,#4d8aa8)" role="img" aria-label="Cable and sensor equipment thumbnail"></div>
  <div class="abs thumb" style="left:581px;background:linear-gradient(#5b7fb4,#b5542e 55%,#d79a5a)" role="img" aria-label="Industrial valves thumbnail"></div>
  <div class="abs thumb" style="left:688px;background:linear-gradient(#3c86d0,#c2552c 50%,#dfe6ee)" role="img" aria-label="Telecom mast thumbnail"></div>
</section>

<section>
  <span class="abs about-rule"></span>
  <h2 class="abs section-title" style="top:634px;font-size:25px">ABOUT <em>VERITRACE</em></h2>
  <p class="abs about-text">Companies have invested to get data out of processes. New technologies have been developed to get real-time data out of the harshest places, like oil-well drill heads or the Great Barrier Riff. Data in itself means nothing without the context the data is collected in. Example: data from equipment under maintenance does not provide information to operations. Information - data which is valid and meaningful - can overwhelm any user without the proper knowledge to interpret this information. Veritrace technology enables easy application of such knowledge in a comprehensible – visual – representation and makes hypothetical reasoning with information possible providing meaningful advisories to subscribers when they need it or when it is required that they are made aware of a situation which requires their attention.</p>
  <a class="abs read-more">READ MORE</a>
</section>

<section>
  <h2 class="abs section-title" style="top:815px;font-size:24px">Our <em>Clients</em></h2>
  <div class="abs clients"></div>
  <span class="abs arrow" style="left:101px"><svg width="6" height="8"><path d="M6 0v8L0 4z" fill="#fff"/></svg></span>
  <span class="abs arrow" style="left:811px"><svg width="6" height="8"><path d="M0 0v8l6-4z" fill="#fff"/></svg></span>
  <span class="abs client" style="left:141px"><i></i>Norvanta</span>
  <span class="abs client" style="left:245px"><i></i>Helix</span>
  <span class="abs client" style="left:334px">Corallo</span>
  <span class="abs client" style="left:420px">Qaswa</span>
  <span class="abs client" style="left:521px"><i></i>Tideline Oil</span>
  <span class="abs client" style="left:672px;font-size:18px">Brouwer</span>
</section>

<footer>
  <div class="abs footer"></div>
  <div class="abs footer-rule"></div>
  <span class="abs follow">Follow Us</span>
  <span class="abs social" style="left:178px" aria-label="Social network link"></span>
  <span class="abs social" style="left:213px" aria-label="Video channel link"></span>
  <span class="abs social" style="left:248px" aria-label="Professional network link"></span>
  <span class="abs news-icon"><svg width="18" height="13" viewBox="0 0 18 13"><rect width="18" height="13" rx="1.5" fill="#e8401c"/><path d="M1 1.5l8 6 8-6" fill="none" stroke="#fff" stroke-width="1.4"/></svg></span>
  <span class="abs news-label">Newsletter Signup</span>
  <span class="abs news-rule"></span>
  <div class="abs email">Email Address</div>
  <div class="abs subscribe">SUBSCRIBE</div>

  <div class="abs col" style="left:102px"><h4>SOLUTIONS</h4><ul><li>Signal Alarm Reporting</li><li>Signal Alarm Analysis</li><li>Signal Alarm Expert</li><li>Rule Studio</li></ul></div>
  <div class="abs col" style="left:253px"><h4>INDUSTRIES</h4><ul><li>Industry</li><li>Telecom</li><li>Power</li><li>Utilities</li><li>Infra</li></ul></div>
  <div class="abs col" style="left:397px"><h4>ABOUT US</h4><ul><li>Company</li><li>Overview</li><li>Leadership</li><li>Partners</li><li>Locations</li></ul></div>
  <div class="abs col" style="left:541px"><h4>NEWS</h4><ul><li>Product News</li><li>Partner News</li><li>Events</li><li>Press Releases</li><li>Vacancies</li></ul></div>
  <div class="abs col contact" style="left:688px"><h4 style="width:140px">CONTACT DETAILS</h4>
    <ul>
      <li><svg width="12" height="12" viewBox="0 0 24 24"><path fill="#e8401c" d="M12 2a7 7 0 0 0-7 7c0 5 7 13 7 13s7-8 7-13a7 7 0 0 0-7-7zm0 9.5a2.5 2.5 0 1 1 0-5 2.5 2.5 0 0 1 0 5z"/></svg><span>Veritrace - Kanaalweg 48,<br>2611 AB<br>Delft</span></li>
      <li><svg width="12" height="12" viewBox="0 0 24 24"><path fill="#e8401c" d="M6.6 10.8a15 15 0 0 0 6.6 6.6l2.2-2.2c.3-.3.7-.4 1-.2 1.1.4 2.3.6 3.6.6.6 0 1 .4 1 1V20c0 .6-.4 1-1 1A17 17 0 0 1 3 4c0-.6.4-1 1-1h3.5c.6 0 1 .4 1 1 0 1.3.2 2.5.6 3.6.1.3 0 .7-.2 1z"/></svg><span>+31 (0)20 5550 184</span></li>
      <li><svg width="12" height="10" viewBox="0 0 18 13"><rect width="18" height="13" rx="1.5" fill="#e8401c"/><path d="M1 1.5l8 6 8-6" fill="none" stroke="#fff" stroke-width="1.4"/></svg><span>hello@veritrace-mail.com</span></li>
    </ul>
    <a class="other">OTHER OFFICES</a>
  </div>
  <div class="abs copyright">© 2015 Veritrace. All Right Reserved.</div>
</footer>

</body>
</html>
```